We are looking for a clean new looking business card.

We would like a new, clean, and modern type business card with our updated contact information. We are a small a plumbing and heating and gasfitting company who offer 24 hr emergency service as well.
We feel our logo looks best on a white background.
Our current cards are outdated, both the design and the information.

Industry/Entity Type

Plumbing and heating

Contact Information for Business Card

Logo, Name, Title, Phone#, Email, Website, "24/7 Emergency Service"

Colors
0054AA
0677BA
7BADD7
CADEEF
E8F1F8

```html
<!DOCTYPE html>
<html lang="en">
<head>
<meta charset="UTF-8">
<title>Clearflow Business Card</title>
<link href="https://fonts.googleapis.com/css2?family=Open+Sans:wght@700;800&family=Poppins:wght@600&family=Arimo:wght@400&display=swap" rel="stylesheet">
<style>
  :root {
    --deep-blue: #0054AA;
    --brand-blue: #0677BA;
    --mid-blue: #1591C8;
    --soft-blue: #7BADD7;
    --pale-blue: #CADEEF;
    --mist-blue: #E8F1F8;
    --ink: #2b2b2b;
    --charcoal: #333436;
    --backdrop: #1c1c1c;
    --rule: #b9b9b9;
  }
  * { margin: 0; padding: 0; box-sizing: border-box; }
  html, body { width: 1200px; height: 1015px; overflow: hidden; }
  body {
    background: var(--backdrop);
    position: relative;
    font-family: "Arimo", Arial, sans-serif;
  }
  .card {
    position: absolute;
    left: 250px;
    width: 700px;
    height: 400px;
    overflow: hidden;
  }

  /* Front */
  .card-front {
    top: 60px;
    background: linear-gradient(30deg, var(--deep-blue) 0%, var(--brand-blue) 30%, #3AA6D6 60%, var(--soft-blue) 82%, var(--pale-blue) 100%);
  }
  .card-front .brand {
    position: absolute;
    left: 48px;
    bottom: 48px;
    color: #fff;
  }
  .brand-name {
    font-family: "Open Sans", sans-serif;
    font-weight: 800;
    letter-spacing: 4px;
    line-height: 1;
    display: flex;
    align-items: center;
    gap: 14px;
    white-space: nowrap;
  }
  .brand-mark {
    display: inline-block;
    width: 0.6em;
    height: 0.6em;
    background: currentColor;
    border-radius: 3px;
  }
  .card-front .brand-name { font-size: 58px; }
  .brand-tagline {
    font-family: "Open Sans", sans-serif;
    font-weight: 700;
    letter-spacing: 4px;
    text-transform: uppercase;
    margin-top: 6px;
    white-space: nowrap;
  }
  .card-front .brand-tagline { font-size: 11px; padding-left: 52px; }

  /* Back */
  .card-back {
    top: 555px;
    background: #fff;
  }
  .card-back .brand {
    position: absolute;
    left: 50px;
    top: 150px;
  }
  .card-back .brand-name {
    font-size: 46px;
    letter-spacing: 3px;
    color: var(--brand-blue);
  }
  .card-back .brand-tagline {
    font-size: 10px;
    letter-spacing: 2.5px;
    color: var(--ink);
    padding-left: 42px;
  }
  .divider {
    position: absolute;
    left: 414px;
    top: 78px;
    width: 1px;
    height: 200px;
    background: var(--rule);
  }
  .contact {
    position: absolute;
    left: 440px;
    top: 82px;
    color: #111;
  }
  .person-name {
    font-family: "Open Sans", sans-serif;
    font-weight: 800;
    font-size: 24px;
    line-height: 1.1;
  }
  .person-name .first { color: var(--brand-blue); }
  .person-name .last { color: var(--ink); }
  .person-title { font-size: 16px; margin-bottom: 22px; }
  .contact-list { list-style: none; }
  .contact-list li {
    display: flex;
    align-items: center;
    gap: 10px;
    font-size: 17px;
    line-height: 1.55;
    white-space: nowrap;
  }
  .contact-list svg { width: 16px; height: 16px; flex: none; }
  .accent { color: var(--brand-blue); }

  .band-blue {
    position: absolute;
    left: 0;
    bottom: 0;
    width: 410px;
    height: 22px;
    background: var(--mid-blue);
  }
  .band-emergency {
    position: absolute;
    right: 0;
    bottom: 0;
    width: 290px;
    height: 58px;
    background: var(--charcoal);
    color: #fff;
    font-family: "Poppins", sans-serif;
    font-weight: 600;
    font-size: 17px;
    letter-spacing: 0.5px;
    display: flex;
    align-items: center;
    justify-content: center;
  }
</style>
</head>
<body>

  <section class="card card-front">
    <div class="brand">
      <div class="brand-name">clearflow</div>
      <div class="brand-tagline">Plumbing · Heating · Gasfitting</div>
    </div>
  </section>

  <section class="card card-back">
    <div class="brand">
      <div class="brand-name"><span class="brand-mark"></span>clearflow</div>
      <div class="brand-tagline">Plumbing · Heating · Gasfitting</div>
    </div>

    <div class="divider"></div>

    <div class="contact">
      <div class="person-name"><span class="first">Daniel</span> <span class="last">Harper</span></div>
      <div class="person-title">Managing Director</div>
      <ul class="contact-list">
        <li>
          <svg viewBox="0 0 24 24" aria-hidden="true"><path fill="var(--brand-blue)" d="M6.6 10.8a15.1 15.1 0 0 0 6.6 6.6l2.2-2.2a1 1 0 0 1 1-.25 11.4 11.4 0 0 0 3.6.57 1 1 0 0 1 1 1V20a1 1 0 0 1-1 1A17 17 0 0 1 3 4a1 1 0 0 1 1-1h3.5a1 1 0 0 1 1 1c0 1.25.2 2.45.57 3.57a1 1 0 0 1-.25 1z"/></svg>
          044-987 654 321
        </li>
        <li>
          <svg viewBox="0 0 24 24" aria-hidden="true"><rect x="2" y="5" width="20" height="14" rx="1" fill="var(--brand-blue)"/><path d="M2.5 6l9.5 7 9.5-7" stroke="#fff" stroke-width="1.6" fill="none"/></svg>
          info@clearflowco.com
        </li>
        <li>
          <svg viewBox="0 0 24 24" aria-hidden="true"><g fill="none" stroke="var(--brand-blue)" stroke-width="1.8"><circle cx="12" cy="12" r="9.5"/><ellipse cx="12" cy="12" rx="4" ry="9.5"/><path d="M2.5 12h19M4 7h16M4 17h16"/></g></svg>
          <span>www.<span class="accent">clearflowpro</span>.com</span>
        </li>
      </ul>
    </div>

    <div class="band-blue"></div>
    <div class="band-emergency">24/7 EMERGENCY SERVICES</div>
  </section>

</body>
</html>
```